New Chirpwall Design Project for a 13.3kW solar system Installed by Talven Energy

We require new artwork for our Chirpwall advertisement of a 13.3kW solar system. Including Morvex 475W N-Type panels and 10kW 1 Phase Pellion inverter. Prices starting from $4799. No sub-contractors. Over 200 + 5 star zentrip reviews. The design is to very clean and not busy. Price and system size is what our customers want. We have always found that the busy designs while conveying a lot of information do not motivate our customers. simple professional designs do however work.

Target Market(s)

homeowners

Industry/Entity Type

solar

Colors
0054AA
0677BA
7BADD7
CADEEF
E8F1F8
EB3D1F
EC4F4E
F09395
F8D3D4
FCEDEE

Requirements
Must have
• must be clean and unbusy design. system size and price is what motivates our customers
Nice to have
• clean pictures of the Morvex 475W N-Type panel and Pellion 10kW 1 Phase inverter.
Should not have
• should not be a busy design with too many words

```html
<!DOCTYPE html>
<html lang="en">
<head>
<meta charset="utf-8">
<title>Talven Energy – 13.3kW Solar System</title>
<link rel="stylesheet" href="https://fonts.googleapis.com/css2?family=Poppins:wght@500;700;800&display=swap">
<style>
  :root {
    --navy: #27303f;
    --red: #c21f2e;
    --red-deep: #b01a28;
    --white: #ffffff;
    --panel-dark: #1c1d21;
    --panel-frame: #c9cacc;
    --sky-top: #f2e4de;
    --sky-mid: #ead8d2;
    --sky-low: #c9c4c6;
    --roof: #8f949c;
  }
  * { margin: 0; padding: 0; box-sizing: border-box; }
  html, body { width: 1200px; height: 1200px; overflow: hidden; }
  body { font-family: "Poppins", sans-serif; background: var(--sky-top); }

  .ad {
    position: relative;
    width: 1200px;
    height: 1200px;
    overflow: hidden;
  }

  .scene-backdrop {
    position: absolute;
    inset: 0;
    background:
      radial-gradient(ellipse 520px 360px at 920px 700px, rgba(255,255,255,0.55), transparent 70%),
      radial-gradient(ellipse 300px 260px at 1120px 560px, rgba(240,196,40,0.55), transparent 75%),
      linear-gradient(180deg, var(--sky-top) 0%, var(--sky-mid) 45%, var(--sky-low) 72%, var(--roof) 100%);
  }

  .red-sweep {
    position: absolute;
    inset: 0;
  }

  .product-panel {
    position: absolute;
    left: 94px;
    top: 133px;
    width: 434px;
    height: 928px;
    background: linear-gradient(180deg, #26272b 0%, var(--panel-dark) 50%, #25262a 100%);
    border: 5px solid var(--panel-frame);
    box-shadow: 0 20px 40px rgba(0,0,0,0.25);
  }

  .brand {
    position: absolute;
    left: 847px;
    top: 78px;
    width: 281px;
    text-align: center;
  }
  .brand-name {
    font-weight: 700;
    font-size: 42px;
    line-height: 1;
    color: var(--red-deep);
    letter-spacing: 1px;
    text-transform: uppercase;
  }
  .brand-tagline {
    margin-top: 10px;
    font-weight: 500;
    font-size: 13px;
    color: var(--navy);
    letter-spacing: 0.3px;
    white-space: nowrap;
    text-transform: uppercase;
  }

  .headline {
    position: absolute;
    left: 600px;
    width: 536px;
    top: 309px;
    text-align: center;
    font-weight: 800;
    text-transform: uppercase;
  }
  .headline-lead {
    display: block;
    font-size: 80px;
    line-height: 80px;
    color: var(--navy);
    letter-spacing: 1px;
  }
  .headline-key {
    display: block;
    font-size: 124px;
    line-height: 124px;
    margin-top: 8px;
    color: var(--red);
    letter-spacing: 10px;
    padding-left: 10px;
  }

  .offer {
    position: absolute;
    left: 600px;
    width: 536px;
    top: 629px;
    text-align: center;
    font-weight: 800;
    text-transform: uppercase;
    color: var(--navy);
  }
  .offer-size {
    font-size: 62px;
    line-height: 64px;
    letter-spacing: 4px;
  }
  .offer-price {
    display: block;
    margin: 21px auto 0;
    width: 520px;
    height: 103px;
    background: var(--red);
    color: var(--white);
    font-size: 78px;
    line-height: 103px;
    letter-spacing: 3px;
    box-shadow: 0 10px 24px rgba(0,0,0,0.18);
  }
</style>
</head>
<body>
  <main class="ad">
    <div class="scene-backdrop" role="img" aria-label="Soft sunset sky over rooftop solar panels with a yellow safety helmet resting on them"></div>

    <svg class="red-sweep" width="1200" height="1200" viewBox="0 0 1200 1200" aria-hidden="true">
      <path d="M0 828 C120 824 210 818 262 826 L1012 1200 L0 1200 Z" fill="var(--red)"/>
    </svg>

    <div class="product-panel" role="img" aria-label="Morvex 475W N-Type black solar panel"></div>

    <header class="brand">
      <p class="brand-name">Talven<br>Energy</p>
      <p class="brand-tagline">Engineered solar for smarter homes</p>
    </header>

    <h1 class="headline">
      <span class="headline-lead">Switch to</span>
      <span class="headline-key">Solar</span>
    </h1>

    <section class="offer">
      <p class="offer-size">13.3kW<br>Solar System</p>
      <p class="offer-price">For $4799!</p>
    </section>
  </main>
</body>
</html>
```